Cool modern, tech Business card design

Looking for a new business card design for our Managed IT Services company. We would like 2 sides, with the logo one one side horizontally and then the information on the back in either vertical or horizontal. We want our colors from the logo incorporated but also would like to see the color gray in there as well.

Target Market(s)

IT, Information Technology, Tech, Service

Industry/Entity Type

It Service

Contact Information for Business Card

Carl Penner
Managing Partner
(P)555-271-4830 ext xxx
(F)555-271-4831
www.brixtelcore.com

Font styles to use
Sans Serif

Colors
959595
000000
ec1f27

Requirements
Must have
• Logo on one side with some nice design or pattern
• Information on back in either vertical or horizontal format
Nice to have
• For it to look cool, tech, modern, stand out.

```html
<!DOCTYPE html>
<html lang="en">
<head>
<meta charset="utf-8">
<title>Brixtelcore Business Card</title>
<link href="https://fonts.googleapis.com/css2?family=Arimo:wght@400;500&display=swap" rel="stylesheet">
<style>
  :root {
    --brand-red: #e50f1a;
    --accent-red: #ec1f27;
    --band-dark: #e8573a;
    --band-mid: #f08a5d;
    --band-light: #fbd3c0;
    --ink: #231f20;
    --gray: #959595;
    --paper: #ffffff;
  }
  html, body {
    margin: 0;
    padding: 0;
    width: 1200px;
    height: 1200px;
    overflow: hidden;
    background: var(--paper);
    font-family: "Arimo", Arial, sans-serif;
  }
  .canvas {
    position: relative;
    width: 1200px;
    height: 1200px;
  }
  .card {
    position: absolute;
    left: 193px;
    width: 850px;
    height: 520px;
    background: var(--paper);
    outline: 1px solid #6d6d6d;
    overflow: hidden;
  }
  .card--info { top: 70px; }
  .card--brand { top: 613px; }
  .card svg.card-art {
    position: absolute;
    inset: 0;
    width: 850px;
    height: 520px;
  }
  .brand-lockup {
    position: absolute;
    display: flex;
    align-items: center;
    color: var(--ink);
    font-weight: 500;
    letter-spacing: -0.5px;
    line-height: 1;
  }
  .brand-lockup .brand-mark {
    background: var(--accent-red);
    border-radius: 4px;
    flex: none;
  }
  .card--info .brand-lockup {
    left: 37px;
    top: 270px;
    font-size: 40px;
    gap: 12px;
  }
  .card--info .brand-mark { width: 18px; height: 18px; }
  .card--brand .brand-lockup {
    left: 0;
    right: 0;
    top: 280px;
    justify-content: center;
    font-size: 76px;
    gap: 20px;
  }
  .card--brand .brand-mark { width: 34px; height: 34px; }
  .contact {
    position: absolute;
    left: 482px;
    top: 0;
    color: var(--ink);
    font-size: 30px;
    white-space: nowrap;
  }
  .contact-line {
    position: absolute;
    left: 0;
    line-height: 1;
    transform: translateY(-50%);
  }
</style>
</head>
<body>
<div class="canvas">

  <section class="card card--info">
    <svg class="card-art" viewBox="0 0 850 520" aria-hidden="true">
      <defs>
        <filter id="soft-shadow" x="-20%" y="-20%" width="140%" height="140%">
          <feGaussianBlur stdDeviation="14"/>
        </filter>
        <radialGradient id="halftone-glow" cx="1" cy="0.5" r="0.9">
          <stop offset="0" stop-color="#ffffff" stop-opacity="0.95"/>
          <stop offset="0.45" stop-color="#ffd6d6" stop-opacity="0.6"/>
          <stop offset="1" stop-color="#e50f1a" stop-opacity="0"/>
        </radialGradient>
      </defs>
      <polygon points="450,-20 850,-20 850,540 450,540 312,260" fill="#959595" opacity="0.55" filter="url(#soft-shadow)"/>
      <polygon points="465,0 850,0 850,520 465,520 328,260" fill="var(--band-mid)"/>
      <polygon points="475,0 850,0 850,520 475,520 338,260" fill="var(--band-light)"/>
      <polygon points="487,0 850,0 850,520 487,520 350,260" fill="var(--band-dark)"/>
      <polygon points="499,0 850,0 850,520 499,520 363,260" fill="var(--brand-red)"/>
      <rect x="620" y="50" width="230" height="440" fill="url(#halftone-glow)" role="img" aria-label="White halftone dot pattern fading into the red panel"/>
      <g class="icon icon--phone" transform="translate(447 258)">
        <circle r="22" fill="none" stroke="#fff" stroke-width="4"/>
        <path d="M-7,-11 l5,-1 3,7 -3,3 c2,4 4,6 8,8 l3,-3 7,3 -1,5 c-12,1 -23,-10 -22,-22z" fill="#fff"/>
      </g>
      <g class="icon icon--pin" transform="translate(447 374)">
        <circle r="22" fill="none" stroke="#fff" stroke-width="4"/>
        <path d="M0,12 c-6,-8 -9,-12 -9,-17 a9,9 0 0 1 18,0 c0,5 -3,9 -9,17z" fill="#fff"/>
        <circle cy="-5" r="3" fill="var(--brand-red)"/>
      </g>
    </svg>

    <div class="brand-lockup">
      <span class="brand-name">brixtelcore</span>
      <span class="brand-mark"></span>
    </div>

    <div class="contact">
      <div class="contact-line" style="top:142px">Carl Penner</div>
      <div class="contact-line" style="top:200px">Managing Partner</div>
      <div class="contact-line" style="top:258px">(P)555-271-4830 ext xxx</div>
      <div class="contact-line" style="top:316px">(F)555-271-4831</div>
      <div class="contact-line" style="top:374px">www.brixtelcore.com</div>
    </div>
  </section>

  <section class="card card--brand">
    <svg class="card-art" viewBox="0 0 850 520" aria-hidden="true">
      <defs>
        <filter id="soft-shadow-b" x="-50%" y="-20%" width="200%" height="140%">
          <feGaussianBlur stdDeviation="14"/>
        </filter>
        <linearGradient id="halftone-left" x1="0" x2="1">
          <stop offset="0" stop-color="#ffffff" stop-opacity="0.8"/>
          <stop offset="1" stop-color="#e50f1a" stop-opacity="0"/>
        </linearGradient>
        <linearGradient id="halftone-right" x1="1" x2="0">
          <stop offset="0" stop-color="#ffffff" stop-opacity="0.8"/>
          <stop offset="1" stop-color="#e50f1a" stop-opacity="0"/>
        </linearGradient>
      </defs>
      <g class="chevron chevron--left">
        <polygon points="0,-20 60,-20 172,260 60,540 0,540" fill="#959595" opacity="0.55" filter="url(#soft-shadow-b)"/>
        <polygon points="0,0 48,0 152,260 48,520 0,520" fill="var(--band-mid)"/>
        <polygon points="0,0 36,0 142,260 36,520 0,520" fill="var(--band-light)"/>
        <polygon points="0,0 22,0 132,260 22,520 0,520" fill="var(--band-dark)"/>
        <polygon points="0,0 10,0 123,260 10,520 0,520" fill="var(--brand-red)"/>
        <rect x="0" y="100" width="70" height="320" fill="url(#halftone-left)" role="img" aria-label="White halftone dot pattern on the red chevron"/>
      </g>
      <g class="chevron chevron--right">
        <polygon points="850,-20 790,-20 678,260 790,540 850,540" fill="#959595" opacity="0.55" filter="url(#soft-shadow-b)"/>
        <polygon points="850,0 802,0 698,260 802,520 850,520" fill="var(--band-mid)"/>
        <polygon points="850,0 814,0 708,260 814,520 850,520" fill="var(--band-light)"/>
        <polygon points="850,0 828,0 718,260 828,520 850,520" fill="var(--band-dark)"/>
        <polygon points="850,0 840,0 727,260 840,520 850,520" fill="var(--brand-red)"/>
        <rect x="780" y="100" width="70" height="320" fill="url(#halftone-right)" role="img" aria-label="White halftone dot pattern on the red chevron"/>
      </g>
    </svg>

    <div class="brand-lockup">
      <span class="brand-name">brixtelcore</span>
      <span class="brand-mark"></span>
    </div>
  </section>

</div>
</body>
</html>
```